Webdesign für Entrümpelungsfirma
Zielgruppe
Unsere Firma heißt Tolvo Hausservice und wir bieten folgende Dienstleistungen an:
Haushaltsauflösungen, Entrümpelungen, Messie-Wohnungen, Demontage-Arbeiten, Gartenpflege.
Aufgabenstellung
Unsere jetzige Seite: www.hausdienst-brenfeld.de
Das Logo bleibt bestehen. Es wäre schön, wenn das neue Design die Farben aufnehmen würde. Es geht erstmal nur um die Startseite.
Die Struktur soll klar und übersichtlich sein.
Wir möchten Vertrauen erwecken, aber nicht langweilig wirken. Das Design soll pfiffig sein und den Kunden aufmerksam machen.
Eine Seite, die uns sehr gut gefällt:
http://www.kramkurt.de/

```html
<!DOCTYPE html>
<html lang="de">
<head>
<meta charset="utf-8">
<title>Tolvo Hausservice – Startseite</title>
<link href="https://fonts.googleapis.com/css2?family=Ubuntu:ital,wght@0,400;0,500;0,700;1,500&family=Open+Sans:wght@400;600;700&display=swap" rel="stylesheet">
<style>
:root{
  --blue:#0a4a9a;
  --blue-text:#1060b0;
  --yellow:#f2c811;
  --green:#b5c114;
  --page:#f2f2f2;
  --white:#ffffff;
  --ink:#222;
  --muted:#555;
}
*{box-sizing:border-box;margin:0;padding:0}
html,body{width:863px;height:1200px;overflow:hidden}
body{background:var(--page);font-family:'Open Sans',sans-serif;color:var(--ink);position:relative}
.site{position:absolute;left:124px;top:0;width:615px;height:1200px;background:var(--white);overflow:hidden}
.abs{position:absolute}

/* top bar */
.topbar{top:0;left:307px;height:19px;display:flex;font-size:7.5px;color:#fff;font-family:'Open Sans',sans-serif}
.topbar .phone{background:var(--yellow);width:94px;display:flex;align-items:center;gap:8px;padding-left:6px}
.topbar .mail{background:var(--blue);width:155px;display:flex;align-items:center;gap:10px;padding-left:6px}
.topbar .social{background:var(--green);width:59px;display:flex;align-items:center;justify-content:space-around;padding:0 6px}
.topbar .social span{width:6px;height:6px;background:#fff;border-radius:50%;opacity:.9}

.brand{top:26px;left:19px;display:flex;align-items:center;gap:10px}
.brand .mark{width:44px;height:44px;border-radius:50%;background:var(--yellow)}
.brand .name{font-family:'Ubuntu',sans-serif;font-weight:500;font-size:22px;color:var(--blue)}

/* nav */
.nav{top:72px;left:0;width:615px;height:20px;background:var(--blue);display:flex;font-size:8px;color:#fff;font-weight:600;letter-spacing:.2px}
.nav a{display:flex;align-items:center;justify-content:center;color:#fff;text-decoration:none}
.nav a.active{background:var(--yellow)}

/* hero */
.hero{top:92px;left:0;width:615px;height:217px;background:linear-gradient(90deg,#dcdcdc,#f1f1f1 45%,#e6e6e6)}
.tag{font-family:'Ubuntu',sans-serif;font-weight:700;color:#fff;display:flex;align-items:center;justify-content:center;box-shadow:2px 3px 6px rgba(0,0,0,.25)}
.tag.y{top:131px;left:501px;width:95px;height:29px;background:var(--yellow);font-size:15px}
.tag.b{top:165px;left:440px;width:156px;height:49px;background:var(--blue);font-size:33px}
.tag.g{top:219px;left:291px;width:305px;height:50px;background:var(--green);font-size:36px}

/* offer bar */
.offer{top:309px;left:0;width:615px;height:36px;background:var(--green)}
.offer .lead{position:absolute;left:57px;top:13px;font-size:8px;color:#fff;font-weight:600}
.offer .lead b{color:var(--blue)}
.field{position:absolute;background:#fff;height:20px;display:flex;align-items:center;font-size:6.5px;color:#b5c114}
.field .ic{width:19px;height:100%;display:flex;align-items:center;justify-content:center;border-right:1px solid #ddd;margin-right:8px}
.offer .btn{position:absolute;left:496px;top:10px;width:56px;height:19px;background:var(--blue);color:#fff;font-size:6.5px;font-weight:700;display:flex;align-items:center;justify-content:center}

/* services */
.h2{font-family:'Ubuntu',sans-serif;font-weight:700;color:var(--blue-text);font-size:14px;letter-spacing:.2px}
.intro{font-size:7.5px;line-height:14.5px;color:var(--ink);z-index:2}
.acc{left:18px;width:190px;height:20px;background:#fff;box-shadow:0 1px 4px rgba(0,0,0,.18);display:flex;align-items:center;font-size:7.5px;font-weight:600;color:#222}
.acc .pm{width:11px;height:11px;border:1px solid var(--blue-text);border-radius:50%;margin:0 9px 0 9px;position:relative}
.acc .pm::before{content:"";position:absolute;left:2px;right:2px;top:4.5px;height:1px;background:var(--blue-text)}
.acc.closed .pm::after{content:"";position:absolute;top:2px;bottom:2px;left:4.5px;width:1px;background:var(--blue-text)}
.sublist{left:44px;top:467px;list-style:none;font-size:6.3px;color:#333}
.sublist li{height:14.3px;display:flex;align-items:center;gap:6px}
.sublist li::before{content:"";width:4px;height:4px;background:var(--blue-text)}
.team{top:385px;left:240px;width:375px;height:252px;background:linear-gradient(180deg,#fff 0%,#f0ede8 40%,#e8eaf0 100%);z-index:1}

/* testimonials */
.reviews{top:637px;left:0;width:615px;height:126px;background:linear-gradient(135deg,#2e63b0,#174d9e 60%,#2a6ac4);color:#fff}
.review{position:absolute;top:17px}
.review .who{font-family:'Ubuntu',sans-serif;font-weight:700;font-size:11px}
.review .city{font-size:7px;margin-top:1px}
.review .stars{color:var(--yellow);font-size:10px;letter-spacing:1px;margin-top:3px}
.review .title{font-family:'Ubuntu',sans-serif;font-style:italic;font-weight:500;font-size:8px;margin-top:12px}
.review p{font-size:7px;line-height:11.7px;margin-top:1px}
.divider{position:absolute;left:225px;top:9px;width:1px;height:108px;background:rgba(255,255,255,.6)}
.arrow{position:absolute;top:56px;color:#fff;font-size:14px}

/* contact */
.card{background:#fff;box-shadow:0 1px 5px rgba(0,0,0,.18);text-align:center}
.card .foot{position:absolute;left:0;bottom:0;width:100%;height:24px;background:var(--blue);color:#fff;font-size:6.5px;display:flex;align-items:center;justify-content:center}
.card .t1{font-size:10px;color:#222}
.card .t2{font-size:7.5px;color:#333;line-height:14px}
.cf{position:absolute;left:18px;width:130px;border:1px solid #ccd;display:flex;align-items:flex-start;font-size:6.5px;color:#999}
.cf .ic{width:20px;height:18px;display:flex;align-items:center;justify-content:center;border-right:1px solid #ddd;margin-right:7px}
.cf span{line-height:18px}
.map{background:linear-gradient(160deg,#e9e8e3,#eeece6 50%,#e5e4df)}

.footer{top:1162px;left:0;width:615px;height:38px;background:var(--yellow);color:#fff;font-size:5.5px;display:flex;align-items:center;justify-content:space-between;padding:0 18px}
.footer .copy{font-size:6.5px;font-weight:600}
</style>
</head>
<body>
<div class="site">

  <div class="abs topbar">
    <div class="phone">
      <svg width="6" height="10" viewBox="0 0 6 10"><rect x=".5" y=".5" width="5" height="9" rx="1" fill="none" stroke="#fff"/></svg>
      07531 44902 17
    </div>
    <div class="mail">
      <svg width="12" height="8" viewBox="0 0 12 8"><rect x=".5" y=".5" width="11" height="7" fill="none" stroke="#fff"/><path d="M.5 .5L6 5 11.5 .5" fill="none" stroke="#fff"/></svg>
      kontakt@tolvo-hausservice.de
    </div>
    <div class="social"><span></span><span></span><span></span></div>
  </div>

  <div class="abs brand">
    <div class="mark"></div>
    <div class="name">Tolvo Hausservice</div>
  </div>

  <nav class="abs nav">
    <a style="width:165px">HAUSHALTSAUFLÖSUNGEN</a>
    <a style="width:137px">ENTRÜMPELUNG / MESSIE</a>
    <a style="width:124px">MÖBELSERVICE</a>
    <a style="width:105px">GARTENPFLEGE</a>
    <a class="active" style="width:84px">KONTAKT</a>
  </nav>

  <div class="abs hero" role="img" aria-label="Umzugskartons vor einer skizzierten Wohnungseinrichtung"></div>
  <div class="abs tag y">Ihr starker</div>
  <div class="abs tag b">Partner</div>
  <div class="abs tag g">rund um’s Haus</div>

  <div class="abs offer">
    <div class="lead">… IHR UNVERBINDLICHES <b>ANGEBOT</b>!</div>
    <div class="field" style="left:220px;top:9px;width:129px">
      <div class="ic"><svg width="10" height="10" viewBox="0 0 10 10"><circle cx="5" cy="3" r="2.5" fill="#b5c114"/><path d="M0 10c0-4 10-4 10 0z" fill="#b5c114"/></svg></div>Name
    </div>
    <div class="field" style="left:358px;top:9px;width:129px">
      <div class="ic"><svg width="11" height="8" viewBox="0 0 11 8"><rect x=".5" y=".5" width="10" height="7" fill="none" stroke="#b5c114"/><path d="M.5 .5L5.5 5 10.5 .5" fill="none" stroke="#b5c114"/></svg></div>Email
    </div>
    <div class="btn">ANFORDERN</div>
  </div>

  <div class="abs team" role="img" aria-label="Drei Mitarbeiter des Teams in weißen Firmen-T-Shirts"></div>

  <div class="abs h2" style="left:18px;top:376px">WIR ERLEDIGEN</div>
  <div class="abs intro" style="left:18px;top:397px;width:222px">alle anfallenden Arbeiten. Haushaltsauflösung, Entrümpelung, Klein-Transporte, Möbel-Montagen.</div>

  <div class="abs acc" style="top:438px"><span class="pm"></span>Haushaltsauflösungen</div>
  <ul class="abs sublist">
    <li>kleine Wohnungen, große Wohnungen</li>
    <li>Studentenzimmer, Senioren-Wohnungen</li>
    <li>Messi-Wohnungen, Keller, Garagen und Werkstätten</li>
    <li>Auch ganze Gebäude</li>
  </ul>
  <div class="abs acc closed" style="top:526px"><span class="pm"></span>Entrümpelung / Messie-Wohnungen</div>
  <div class="abs acc closed" style="top:553px"><span class="pm"></span>Möbelservice</div>
  <div class="abs acc closed" style="top:578px"><span class="pm"></span>Gartenservice</div>

  <section class="abs reviews">
    <div class="arrow" style="left:10px">‹</div>
    <div class="review" style="left:34px;width:180px">
      <div class="who">Helga Brinkmann</div>
      <div class="city">Brenfeld</div>
      <div class="stars">★★★★★</div>
      <div class="title">Teil-Räumung und Transporte</div>
      <p>Alles ist sehr gut abgelaufen. Sehr empfehlenswert.</p>
    </div>
    <div class="divider"></div>
    <div class="review" style="left:246px;width:336px">
      <div class="who">T. Albrecht</div>
      <div class="city">Halbach</div>
      <div class="stars">★★★★★</div>
      <div class="title">Wohnungsauflösung in Halbach</div>
      <p>Bei der Auflösung meiner Zweitwohnung in Halbach habe ich die Firma Tolvo Hausservice beauftragt. Der Termin kam sehr kurzfristig zu Stande, die Arbeit wurde aufs Beste erledigt und auf kurzfristige Wünsche wurden schnell und zuvorkommend eingegangen.</p>
    </div>
    <div class="arrow" style="left:597px">›</div>
  </section>

  <div class="abs h2" style="left:19px;top:794px">KONTAKTIEREN SIE UNS!</div>
  <div class="abs intro" style="left:19px;top:815px">Tolvo Hausservice: Ihr starker Partner rund um’s Haus</div>

  <div class="abs card" style="left:36px;top:848px;width:166px;height:135px">
    <svg style="margin-top:14px" width="26" height="36" viewBox="0 0 26 36"><path d="M13 0C5.8 0 0 5.8 0 13c0 9 13 23 13 23s13-14 13-23C26 5.8 20.2 0 13 0z" fill="#0a4a9a"/><circle cx="13" cy="12" r="6" fill="#fff"/></svg>
    <div class="t1" style="margin-top:8px">Wendland GmbH</div>
    <div class="t2" style="margin-top:3px">Lindenweg 12/4<br>D-78462 Brenfeld</div>
    <div class="foot"></div>
  </div>

  <div class="abs card" style="left:211px;top:848px;width:166px;height:135px">
    <div class="cf" style="top:14px;height:20px"><div class="ic"><svg width="9" height="10" viewBox="0 0 10 10"><circle cx="5" cy="3" r="2.5" fill="#0a4a9a"/><path d="M0 10c0-4 10-4 10 0z" fill="#0a4a9a"/></svg></div><span>Name</span></div>
    <div class="cf" style="top:37px;height:20px"><div class="ic"><svg width="11" height="8" viewBox="0 0 11 8"><rect x=".5" y=".5" width="10" height="7" fill="#0a4a9a"/><path d="M.5 .5L5.5 5 10.5 .5" fill="none" stroke="#fff"/></svg></div><span>Email</span></div>
    <div class="cf" style="top:60px;height:37px"><div class="ic"><svg width="10" height="8" viewBox="0 0 10 8"><path d="M0 .5h10M0 3h10M0 5.5h10M0 7.5h7" stroke="#0a4a9a"/></svg></div><span>Ihre Nachricht an uns</span></div>
    <div class="foot">SENDEN</div>
  </div>

  <div class="abs card" style="left:36px;top:993px;width:166px;height:134px">
    <svg style="margin-top:14px" width="22" height="36" viewBox="0 0 22 36"><rect x="0" y="0" width="22" height="36" rx="3" fill="#0a4a9a"/><rect x="3" y="4" width="16" height="24" fill="#fff"/><circle cx="11" cy="32" r="1.6" fill="#fff"/></svg>
    <div class="t1" style="margin-top:8px">07531 44902 17</div>
    <div class="t2" style="margin-top:3px">Fax 07531 449 0218<br>kontakt@tolvo-hausservice.de</div>
    <div class="foot"></div>
  </div>

  <div class="abs map" style="left:386px;top:848px;width:229px;height:279px" role="img" aria-label="Straßenkarte mit Standort der Firma"></div>
  <div class="abs map" style="left:211px;top:993px;width:175px;height:134px" role="img" aria-label="Straßenkarte mit Standort der Firma"></div>

  <footer class="abs footer">
    <div>HOME &nbsp;|&nbsp; ÜBER UNS &nbsp;|&nbsp; PREISE &nbsp;|&nbsp; KONTAKT &nbsp;|&nbsp; IMPRESSUM</div>
    <div class="copy">Copyright © 2016 Tolvo Hausservice</div>
    <div>ZURÜCK NACH OBEN</div>
  </footer>

</div>
</body>
</html>
```